Business Card Design

Electronic Security Installation Specialists

Check out our website at www.bramblecoastllc.com to see what we do.

Industry/Entity Type

Business

Contact Information for Business Card

Fern Ridge
Marisol Penton
318 Calloway Drive
Harlow Springs, WV 26118

Colors
3176b5
0455a3
ffffff

```html
<!DOCTYPE html>
<html lang="en">
<head>
<meta charset="utf-8">
<title>Fern Ridge Business Card</title>
<link href="https://fonts.googleapis.com/css2?family=Open+Sans:wght@400;600;700&display=swap" rel="stylesheet">
<style>
  :root {
    --brand-blue: #3176b5;
    --brand-deep: #0455a3;
    --paper: #ffffff;
    --ink: #222a33;
    --muted: #5d6670;
    --rule: #3176b5;
    --backdrop: #e9ebee;
  }
  * { box-sizing: border-box; margin: 0; padding: 0; }
  html, body {
    width: 1200px; height: 913px; overflow: hidden;
    background: var(--backdrop);
    font-family: "Open Sans", Arial, sans-serif;
  }
  .stage {
    position: relative; width: 1200px; height: 913px;
    display: flex; align-items: center; justify-content: center; gap: 40px;
  }
  .card {
    position: relative; width: 520px; height: 297px;
    background: var(--paper);
    box-shadow: 0 10px 28px rgba(0,0,0,.18), 0 2px 6px rgba(0,0,0,.1);
    overflow: hidden;
  }
  .brand-mark {
    display: flex; align-items: center; gap: 12px;
    color: var(--brand-deep); font-weight: 700; white-space: nowrap;
  }
  .brand-mark .dot {
    border-radius: 50%; background: var(--brand-blue); flex: none;
  }
  .card-front .brand-mark {
    position: absolute; left: 50%; top: 50%; transform: translate(-50%, -50%);
    font-size: 34px;
  }
  .card-front .brand-mark .dot { width: 44px; height: 44px; }

  .card-back .bottom-band {
    position: absolute; left: 0; right: 0; bottom: 0; height: 9px;
    background: linear-gradient(90deg, var(--brand-deep), var(--brand-blue));
  }
  .person { position: absolute; right: 26px; top: 30px; text-align: right; }
  .person-name { color: var(--brand-blue); font-weight: 700; font-size: 17px; line-height: 1.2; }
  .person-title { color: var(--muted); font-size: 11px; margin-top: 2px; }
  .top-rule {
    position: absolute; right: 26px; top: 84px; width: 290px; height: 1px; background: var(--rule);
  }
  .address {
    position: absolute; right: 26px; top: 100px; text-align: right;
    font-size: 11px; line-height: 1.45; color: var(--ink); font-style: normal;
  }
  .card-back .brand-mark {
    position: absolute; left: 28px; top: 128px; font-size: 22px; gap: 9px;
  }
  .card-back .brand-mark .dot { width: 30px; height: 30px; }
  .contact-rule {
    position: absolute; left: 22px; top: 204px; width: 240px; height: 1px; background: var(--rule);
  }
  .contact-list {
    position: absolute; left: 24px; top: 212px; list-style: none;
    font-size: 12px; line-height: 1.5; color: var(--ink);
  }
  .contact-list li { display: flex; align-items: center; gap: 8px; }
  .contact-list svg { width: 11px; height: 11px; fill: var(--ink); flex: none; }
  .contact-list .web { color: var(--brand-blue); font-weight: 600; }
</style>
</head>
<body>
<main class="stage">
  <section class="card card-front" aria-label="Card front">
    <div class="brand-mark"><span class="dot"></span>Fern Ridge</div>
  </section>

  <section class="card card-back" aria-label="Card back">
    <div class="person">
      <div class="person-name">Marisol Penton</div>
      <div class="person-title">Managing Director</div>
    </div>
    <div class="top-rule"></div>
    <address class="address">
      318 Calloway Drive<br>Harlow Springs, WV 26118
    </address>

    <div class="brand-mark"><span class="dot"></span>Fern Ridge</div>

    <div class="contact-rule"></div>
    <ul class="contact-list">
      <li>
        <svg viewBox="0 0 16 16" aria-hidden="true"><path d="M3 1h3l1.5 4-2 1.3a9 9 0 0 0 4.2 4.2L11 8.5l4 1.5v3a2 2 0 0 1-2 2A12 12 0 0 1 1 3a2 2 0 0 1 2-2z"/></svg>
        304-555-0182
      </li>
      <li>
        <svg viewBox="0 0 16 16" aria-hidden="true"><path d="M8 0a8 8 0 1 0 0 16A8 8 0 0 0 8 0zm0 1.5c.9 0 2 1.9 2.3 5H5.7C6 3.4 7.1 1.5 8 1.5zM1.6 7h2.6a13 13 0 0 0 .4 3H2.2a6.5 6.5 0 0 1-.6-3zm10.2 0h2.6a6.5 6.5 0 0 1-.6 3h-2.4a13 13 0 0 0 .4-3zM5.7 7h4.6a12 12 0 0 1-.4 3H6.1a12 12 0 0 1-.4-3zm.5 4.5h3.6c-.5 1.8-1.2 3-1.8 3s-1.3-1.2-1.8-3z"/></svg>
        m.penton@bramblecoastllc.com
      </li>
      <li>
        <svg viewBox="0 0 16 16" aria-hidden="true"><path d="M1 3h14v10H1zM2 4.2v.3l6 4.3 6-4.3v-.3z"/></svg>
        <span class="web">www.bramblecoastllc.com</span>
      </li>
    </ul>
    <div class="bottom-band"></div>
  </section>
</main>
</body>
</html>
```